Baby Making Project

We need a poster design for a surrogacy/ivf clinic. We would like the poster to be used as office artwork and to say something like

'We came here as a couple, we left as a family'

The poster should have some family related picture in it, but not necessarily the standard mother, father and child image.
The services are used by many single and gay parents so we don't want to alienate anyone.
The poster should like modern, perhaps with the use of animals photo, or animated looking characters so you can't make out whether the parents are male/female.

Baby

```html
<!DOCTYPE html>
<html lang="en">
<head>
<meta charset="utf-8">
<title>We came here as a couple, we left as a family</title>
<link rel="stylesheet" href="https://fonts.googleapis.com/css2?family=Great+Vibes&family=Yesteryear&display=swap">
<style>
  :root {
    --cream: #fdfbe3;
    --cream-deep: #f8f1cf;
    --orange: #e8821e;
    --orange-soft: #f4b25a;
    --gold: #f7cf5a;
    --brown: #3a2216;
    --bear-light: #ecdcb8;
    --bear-mid: #d6bb87;
    --bear-deep: #b8935a;
  }
  html, body {
    margin: 0;
    padding: 0;
    width: 848px;
    height: 1200px;
    overflow: hidden;
    background: var(--cream);
  }
  .poster {
    position: relative;
    width: 848px;
    height: 1200px;
    overflow: hidden;
    background: linear-gradient(180deg, var(--cream) 0%, var(--cream-deep) 100%);
  }
  .teddy-photo {
    position: absolute;
    left: 0;
    top: 480px;
    width: 848px;
    height: 720px;
    background:
      radial-gradient(ellipse 200px 230px at 170px 330px, var(--bear-light) 0%, transparent 100%),
      radial-gradient(ellipse 210px 260px at 390px 240px, var(--bear-mid) 0%, transparent 100%),
      radial-gradient(ellipse 260px 320px at 680px 330px, var(--bear-deep) 0%, transparent 100%),
      linear-gradient(180deg, var(--cream-deep), var(--bear-mid));
    -webkit-mask-image: linear-gradient(180deg, transparent 0%, #000 30%);
    mask-image: linear-gradient(180deg, transparent 0%, #000 30%);
  }
  .wave {
    position: absolute;
    left: 0;
    width: 848px;
  }
  .wave--top { top: 0; height: 170px; }
  .wave--bottom { bottom: 0; height: 180px; }
  .headline {
    margin: 0;
    font-weight: normal;
  }
  .headline span {
    position: absolute;
    white-space: nowrap;
    line-height: 1;
  }
  .headline .accent {
    font-family: "Great Vibes", cursive;
    color: var(--orange);
    text-shadow: 1px 1px 0 #fff3d6, 2px 2px 2px rgba(120, 60, 10, 0.25);
  }
  .headline .phrase {
    font-family: "Yesteryear", cursive;
    color: var(--brown);
    text-shadow: 2px 2px 0 #c9b9a4;
  }
  .word-we { left: 300px; top: 80px; font-size: 190px; }
  .word-came { left: 605px; top: 160px; font-size: 64px; }
  .line-couple { left: 28px; top: 290px; font-size: 78px; letter-spacing: 1px; }
  .line-as-a { left: 28px; top: 430px; font-size: 78px; }
  .word-family { left: 235px; top: 375px; font-size: 200px; }
</style>
</head>
<body>
<main class="poster">
  <div class="teddy-photo" role="img" aria-label="Soft-focus photo of three fluffy teddy bears of different sizes sitting together, one with a bow tie and one with a ribbon bow"></div>

  <svg class="wave wave--top" viewBox="0 0 848 170" preserveAspectRatio="none" aria-hidden="true">
    <path d="M0 0 H848 V40 C700 20 520 70 300 60 C180 55 80 80 0 110 Z" fill="var(--orange-soft)" opacity="0.55"/>
    <path d="M0 0 H600 C460 10 300 60 160 70 C90 75 40 85 0 95 Z" fill="var(--orange)" opacity="0.85"/>
    <path d="M0 110 C150 70 360 45 560 20 C680 8 780 15 848 30" fill="none" stroke="var(--gold)" stroke-width="6" opacity="0.8"/>
    <path d="M0 150 C200 100 420 55 620 30 C720 20 800 40 848 70" fill="none" stroke="var(--gold)" stroke-width="3" opacity="0.7"/>
    <path d="M848 40 C800 60 780 100 848 150" fill="none" stroke="var(--gold)" stroke-width="4" opacity="0.6"/>
  </svg>

  <svg class="wave wave--bottom" viewBox="0 0 848 180" preserveAspectRatio="none" aria-hidden="true">
    <path d="M0 20 C200 40 420 110 848 120 V180 H0 Z" fill="var(--orange-soft)" opacity="0.6"/>
    <path d="M0 70 C180 70 360 140 620 180 H0 Z" fill="var(--orange)" opacity="0.85"/>
    <path d="M0 40 C260 60 520 130 848 100" fill="none" stroke="var(--gold)" stroke-width="5" opacity="0.8"/>
    <path d="M0 100 C260 100 520 150 848 130" fill="none" stroke="var(--gold)" stroke-width="3" opacity="0.7"/>
    <path d="M848 0 C760 40 700 90 848 170" fill="none" stroke="var(--gold)" stroke-width="4" opacity="0.7"/>
  </svg>

  <h1 class="headline">
    <span class="accent word-we">We</span>
    <span class="phrase word-came">came</span>
    <span class="phrase line-couple">here as a couple, we left</span>
    <span class="phrase line-as-a">as a</span>
    <span class="accent word-family">Family</span>
  </h1>
</main>
</body>
</html>
```